Torvane Travel Business Card Design

We need a new business card design for our travel agency business - Torvane Travel. We design packages to some of the most popular travel destinations in the world for groups, individuals and also tailor-make personalised packages. Our logo attached must be used. On the back of the card we would like a list of all websites under our Torvane brand to be posted. We would like clean, modern, simple design.

Industry/Entity Type

Travel Agent

Contact Information for Business Card

Owen Pridmore
National Sales Manager
Reservations: 1300 742 689
Tel: 61 28473 5096
Fax: 61 2847 3971
Email: owen@torvanetravel.com.au
Web: www.torvanetravel.com.au

Address: Level 1, 417 Harwick Street
Sydney NSW 2000 Australia

Requirements
Must have
• On the back of the card we want all websites listed under our Torvane brand.
• Torvane Travel Group - Wholesale Specialists
• www.qpjourneys.com.au - New Caledonia
• www.bravelmijourneys.com.au - Tahiti
• www.sorvenbreakhub.com.au - China
Nice to have
• Modern, clean lined, simple and fresh
Should not have
• Look dull

```html
<!DOCTYPE html>
<html lang="en">
<head>
<meta charset="utf-8">
<title>Torvane Travel Business Card</title>
<link href="https://fonts.googleapis.com/css2?family=Roboto+Condensed:wght@400;700&display=swap" rel="stylesheet">
<style>
  :root {
    --backdrop: #dde3e1;
    --card: #ffffff;
    --brand-blue: #2f3ba3;
    --brand-red: #ea3f5c;
    --faint-grey: #e6e8ea;
    --card-shadow: rgba(40, 55, 60, 0.18);
  }
  * { box-sizing: border-box; margin: 0; padding: 0; }
  html, body {
    width: 1200px;
    height: 1000px;
    overflow: hidden;
    background: var(--backdrop);
    font-family: "Roboto Condensed", "Arial Narrow", sans-serif;
  }
  .stage { position: relative; width: 1200px; height: 1000px; }

  .business-card {
    position: absolute;
    width: 580px;
    height: 350px;
    background: var(--card);
    border-radius: 4px;
    box-shadow: 0 10px 28px var(--card-shadow);
  }
  .card-front { left: 120px; top: 130px; }
  .card-back { left: 500px; top: 520px; }

  /* Front */
  .brand-name {
    position: absolute;
    left: 40px;
    top: 64px;
    display: flex;
    align-items: center;
    gap: 10px;
    font-size: 38px;
    font-weight: 700;
    color: var(--brand-blue);
    letter-spacing: -0.5px;
  }
  .brand-dot {
    width: 14px;
    height: 14px;
    border-radius: 50%;
    background: var(--brand-red);
  }
  .person {
    position: absolute;
    left: 40px;
    top: 178px;
    line-height: 1.25;
  }
  .person-name { font-size: 21px; font-weight: 700; color: var(--brand-red); }
  .person-title { font-size: 21px; font-weight: 700; color: var(--brand-blue); }
  .person-email { font-size: 16px; color: var(--brand-blue); margin-top: 2px; }
  .company-web {
    position: absolute;
    left: 40px;
    top: 290px;
    font-size: 16px;
    font-weight: 700;
    color: var(--brand-red);
  }
  .contact-list {
    position: absolute;
    left: 320px;
    top: 54px;
    list-style: none;
  }
  .contact-item {
    display: flex;
    gap: 12px;
    font-size: 15px;
    line-height: 1.35;
    color: var(--brand-blue);
    margin-bottom: 26px;
  }
  .contact-icon { width: 16px; height: 18px; flex: none; margin-top: 14px; }

  /* Back */
  .aircraft-area {
    position: absolute;
    left: 40px;
    top: 40px;
    width: 300px;
    height: 230px;
    border-radius: 48% 52% 44% 56%;
    background: radial-gradient(ellipse at center, var(--faint-grey) 0%, #f0f1f2 60%, var(--card) 100%);
  }
  .brand-sites {
    position: absolute;
    right: 36px;
    bottom: 90px;
    list-style: none;
    text-align: right;
    font-size: 16px;
    line-height: 1.45;
    font-weight: 700;
  }
  .site-url { color: var(--brand-blue); }
  .site-destination { color: var(--brand-red); }
</style>
</head>
<body>
<main class="stage">

  <section class="business-card card-front" aria-label="Business card front">
    <div class="brand-name"><span>Torvane Travel</span><span class="brand-dot"></span></div>

    <div class="person">
      <p class="person-name">Owen Pridmore</p>
      <p class="person-title">National Sales Manager</p>
      <p class="person-email">owen@torvanetravel.com.au</p>
    </div>

    <p class="company-web">www.torvanetravel.com.au</p>

    <ul class="contact-list">
      <li class="contact-item">
        <svg class="contact-icon" viewBox="0 0 16 20" aria-hidden="true">
          <path d="M8 0C3.6 0 0 3.4 0 7.6 0 13 8 20 8 20s8-7 8-12.4C16 3.4 12.4 0 8 0z" fill="var(--brand-red)"/>
          <circle cx="8" cy="7.5" r="3" fill="#fff"/>
        </svg>
        <span>Level 1, 417 Harwick Street<br>Sydney NSW 2000 Australia</span>
      </li>
      <li class="contact-item">
        <svg class="contact-icon" viewBox="0 0 20 20" aria-hidden="true" style="margin-top:26px">
          <path d="M4.5 1.5l3 3.2-1.8 2.4c1.2 2.6 3.2 4.6 5.8 5.8l2.4-1.8 3.2 3-2 3.1C8.3 17 3 11.7 1.6 3.8z" fill="var(--brand-red)"/>
        </svg>
        <span>Reservations: 1300 742 689<br>Tel: 61 28473 5096<br>Fax: 61 2847 3971</span>
      </li>
    </ul>
  </section>

  <section class="business-card card-back" aria-label="Business card back">
    <div class="aircraft-area" role="img" aria-label="Faint grey aircraft silhouette decoration"></div>
    <ul class="brand-sites">
      <li><span class="site-url">www.bravelmijourneys.com.au</span> - <span class="site-destination">TAHITI</span></li>
      <li><span class="site-url">www.sorvenbreakhub.com.au</span> - <span class="site-destination">CHINA</span></li>
      <li><span class="site-url">www.qpjourneys.com.au</span> - <span class="site-destination">NEW CALEDONIA</span></li>
    </ul>
  </section>

</main>
</body>
</html>
```